Powerpoint Presentation Template

Kindly design a business class Powepoint Presentation template for our business use. Please stick to our company colours or even pictures as shown on our website and Logo

```html
<!DOCTYPE html>
<html lang="en">
<head>
<meta charset="utf-8">
<title>Kavora Properties – Presentation Template</title>
<link href="https://fonts.googleapis.com/css2?family=Open+Sans:wght@400;600;700&family=Oswald:wght@600&display=swap" rel="stylesheet">
<style>
:root{
  --maroon:#8e3a2b;
  --maroon-dark:#6f2a1f;
  --black:#141414;
  --slate:#3a3d43;
  --ink:#333;
  --muted:#8a8a8a;
  --page:#ffffff;
  --line:#e4e4e4;
}
*{box-sizing:border-box;margin:0;padding:0}
html,body{width:1059px;height:1200px;overflow:hidden;background:var(--page);font-family:"Open Sans",Arial,sans-serif;color:var(--ink)}
.deck{position:relative;width:1059px;height:1200px}
.slide{position:absolute;width:345px;height:194px;background:#fff;overflow:hidden;box-shadow:0 1px 3px rgba(0,0,0,.25)}
.abs{position:absolute}
.s-title{position:absolute;left:15px;top:14px;font-size:11px;color:var(--maroon);letter-spacing:.2px}
.corner{position:absolute;right:0;top:0;width:30px;height:30px}
.foot-logo{position:absolute;left:16px;bottom:5px;font-size:4.5px;font-weight:700;color:var(--maroon);line-height:1}
.foot-logo span{display:block;font-weight:400;color:var(--ink);font-size:3.5px}
.foot-copy{position:absolute;left:0;right:0;bottom:6px;text-align:center;font-size:3px;color:#aaa}
.ph{position:absolute}
.ph-sky{background:linear-gradient(180deg,#9fb4c9 0%,#c8c2b8 55%,#8d7a68 100%)}
.ph-int{background:linear-gradient(160deg,#7a3026 0%,#3a2a28 60%,#1e1e1e 100%)}
.ph-site{background:linear-gradient(180deg,#a8bccd 0%,#b7a58d 50%,#9b5b3c 100%)}
.ph-home{background:linear-gradient(180deg,#d9d3ca 0%,#b9aea0 60%,#8a7f74 100%)}
.ph-grey{background:linear-gradient(180deg,#bdbdbd 0%,#8c8c8c 60%,#5a5a5a 100%)}
.ph-road{background:linear-gradient(180deg,#9db3c4 0%,#7e8a7a 45%,#5e5e5e 100%)}
.tiny{font-size:3.6px;line-height:1.35;color:#777}
.white{color:#fff}
.cell-text{position:absolute;padding:5px 6px;color:#fff}
.cell-text h4{font-size:5px;font-weight:700;margin-bottom:4px}
.cell-text p{font-size:4.2px;line-height:1.35}
.num{font-size:12px;font-weight:600;text-align:center;display:block;margin-top:14px}
.ph-label{font-size:3.6px;text-align:center;display:block;font-weight:700}
.client{position:absolute;font-size:9px;font-weight:600;color:#2b2b2b;text-align:center;width:70px}
</style>
</head>
<body>
<div class="deck">

<!-- 1 Cover -->
<section class="slide" style="left:4px;top:3px">
  <div class="ph ph-grey" style="left:0;top:0;width:345px;height:194px" role="img" aria-label="Photograph of a completed office building with construction workers"></div>
  <svg class="abs" style="left:0;top:0" width="345" height="194" aria-hidden="true"><polygon points="215,0 345,0 345,194 150,194 205,110" fill="#8e3a2b" opacity=".88"/></svg>
  <div class="abs" style="left:18px;top:28px;font-size:12px;font-weight:700;color:var(--maroon);line-height:1">KAVORA<span style="display:block;font-weight:400;font-size:9px;color:#333">Properties</span></div>
  <div class="abs white" style="left:200px;top:54px;font-family:Oswald,sans-serif;font-size:19px;line-height:1.05;text-align:right;width:92px">ACHIEVING DISTINCTION</div>
  <div class="abs white" style="left:200px;top:98px;width:92px;text-align:right;font-size:3.5px;line-height:1.5;font-weight:700">BUILDING CONSTRUCTION<br>ROAD &amp; CIVIL CONSTRUCTION<br>PROPERTY DEVELOPMENT</div>
</section>

<!-- 2 Title -->
<section class="slide" style="left:357px;top:3px">
  <div class="ph ph-road" style="left:0;top:0;width:345px;height:194px" role="img" aria-label="Photograph of a road under construction lined with trees"></div>
  <svg class="abs" style="left:0;top:0" width="345" height="194" aria-hidden="true">
    <polygon points="0,120 60,70 120,140 180,85 260,150 345,100 345,194 0,194" fill="#8e3a2b" opacity=".9"/>
    <polygon points="0,150 80,110 150,165 240,120 345,160 345,194 0,194" fill="#6f2a1f"/>
  </svg>
  <div class="abs" style="right:52px;top:14px;font-size:9px;font-weight:700;color:var(--maroon);text-align:right;line-height:1">KAVORA<span style="display:block;font-weight:400;font-size:6px;color:#222">Properties</span></div>
  <div class="abs white" style="right:20px;top:141px;font-size:14px">Your Title Goes Here</div>
  <div class="abs white" style="right:20px;top:160px;font-size:7px">Your Subtitle Here</div>
</section>

<!-- 3 Agenda -->
<section class="slide" style="left:710px;top:3px;background:var(--maroon)">
  <div class="abs white" style="left:15px;top:13px;font-size:11px">Agenda</div>
  <svg class="abs" style="left:0;top:0" width="345" height="194" aria-hidden="true" font-family="Open Sans, sans-serif" font-size="7" fill="#fff" text-anchor="middle">
    <g><circle cx="75" cy="60" r="9" fill="#141414"/><text x="75" y="63">1</text><text x="75" y="82" font-size="6">Agenda 1</text></g>
    <g><circle cx="146" cy="60" r="9" fill="#141414"/><text x="146" y="63">2</text><text x="146" y="82" font-size="6">Agenda 2</text></g>
    <g><circle cx="213" cy="60" r="9" fill="#141414"/><text x="213" y="63">3</text><text x="213" y="82" font-size="6">Agenda 3</text></g>
    <g><circle cx="281" cy="60" r="9" fill="#141414"/><text x="281" y="63">4</text><text x="281" y="82" font-size="6">Agenda 4</text></g>
    <g><circle cx="75" cy="130" r="9" fill="#141414"/><text x="75" y="133">5</text><text x="75" y="152" font-size="6">Agenda 5</text></g>
    <g><circle cx="146" cy="130" r="9" fill="#141414"/><text x="146" y="133">6</text><text x="146" y="152" font-size="6">Agenda 6</text></g>
    <g><circle cx="213" cy="130" r="9" fill="#141414"/><text x="213" y="133">7</text><text x="213" y="152" font-size="6">Agenda 7</text></g>
    <g><circle cx="281" cy="130" r="9" fill="#141414"/><text x="281" y="133">8</text><text x="281" y="152" font-size="6">Agenda 8</text></g>
  </svg>
</section>

<!-- 4 Your Agenda -->
<section class="slide" style="left:4px;top:203px">
  <svg class="abs" style="left:0;top:0" width="345" height="194" aria-hidden="true" font-family="Open Sans, sans-serif">
    <polygon points="0,0 120,0 170,194 0,194" fill="#8e3a2b"/>
    <line x1="124" y1="0" x2="174" y2="194" stroke="#8e3a2b" stroke-width="2"/>
    <g font-size="5" fill="#fff">
      <polygon points="185,35 285,35 292,46 185,46" fill="#8e3a2b"/><circle cx="185" cy="40.5" r="8" fill="#fff" stroke="#8e3a2b"/><text x="183" y="42.5" fill="#8e3a2b">1</text><text x="197" y="42.5">Lorem Ipsum Dolor Sit</text>
      <polygon points="190,57 290,57 297,68 190,68" fill="#8e3a2b"/><circle cx="190" cy="62.5" r="8" fill="#fff" stroke="#8e3a2b"/><text x="188" y="64.5" fill="#8e3a2b">2</text><text x="202" y="64.5">Lorem Ipsum Dolor Sit</text>
      <polygon points="195,79 295,79 302,90 195,90" fill="#8e3a2b"/><circle cx="195" cy="84.5" r="8" fill="#fff" stroke="#8e3a2b"/><text x="193" y="86.5" fill="#8e3a2b">3</text><text x="207" y="86.5">Lorem Ipsum Dolor Sit</text>
      <polygon points="200,101 300,101 307,112 200,112" fill="#8e3a2b"/><circle cx="200" cy="106.5" r="8" fill="#fff" stroke="#8e3a2b"/><text x="198" y="108.5" fill="#8e3a2b">4</text><text x="212" y="108.5">Lorem Ipsum Dolor Sit</text>
      <polygon points="205,123 305,123 312,134 205,134" fill="#8e3a2b"/><circle cx="205" cy="128.5" r="8" fill="#fff" stroke="#8e3a2b"/><text x="203" y="130.5" fill="#8e3a2b">5</text><text x="217" y="130.5">Lorem Ipsum Dolor Sit</text>
      <polygon points="210,145 310,145 317,156 210,156" fill="#8e3a2b"/><circle cx="210" cy="150.5" r="8" fill="#fff" stroke="#8e3a2b"/><text x="208" y="152.5" fill="#8e3a2b">6</text><text x="222" y="152.5">Lorem Ipsum Dolor Sit</text>
    </g>
  </svg>
  <div class="abs white" style="left:18px;top:126px;font-size:14px">Your Agenda</div>
</section>

<!-- 5 About Us -->
<section class="slide" style="left:357px;top:203px">
  <div class="s-title">ABOUT US</div>
  <svg class="corner" viewBox="0 0 30 30" aria-hidden="true"><polygon points="0,0 30,0 30,30" fill="#8e3a2b"/><text x="24" y="9" font-size="4" fill="#fff">5</text></svg>
  <div class="abs tiny" style="left:20px;top:48px;width:305px;text-align:justify">We build homes, roads and workplaces that last for generations. Our teams plan every project with care, from the first survey to the final handover, and we keep clients informed at each stage. Quality materials, skilled crews and strict safety standards guide everything we do on site. We believe good construction strengthens whole communities and creates lasting value for owners and tenants alike.</div>
  <div class="abs tiny" style="left:20px;top:87px;width:305px;text-align:justify">We build homes, roads and workplaces that last for generations. Our teams plan every project with care, from the first survey to the final handover, and we keep clients informed at each stage. Quality materials, skilled crews and strict safety standards guide everything we do on site. We believe good construction strengthens whole communities and creates lasting value for owners and tenants alike.</div>
  <div class="abs tiny" style="left:20px;top:126px;width:305px;text-align:justify">We build homes, roads and workplaces that last for generations. Our teams plan every project with care, from the first survey to the final handover, and we keep clients informed at each stage. Quality materials, skilled crews and strict safety standards guide everything we do on site. We believe good construction strengthens whole communities and creates lasting value for owners and tenants alike.</div>
  <div class="foot-logo">KAVORA<span>Properties</span></div>
  <div class="foot-copy">© Copyright 2024 Kavora. All rights reserved.</div>
</section>

<!-- 6 Bullets -->
<section class="slide" style="left:710px;top:203px">
  <div class="s-title">BULLETS POINT 1 LEVEL</div>
  <svg class="corner" viewBox="0 0 30 30" aria-hidden="true"><polygon points="0,0 30,0 30,30" fill="#8e3a2b"/><text x="24" y="9" font-size="4" fill="#fff">6</text></svg>
  <svg class="abs" style="left:0;top:0" width="345" height="194" aria-hidden="true">
    <circle cx="29" cy="55" r="2.3" fill="#8e3a2b"/><circle cx="138" cy="55" r="2.3" fill="#141414"/><circle cx="246" cy="55" r="2.3" fill="#141414"/>
    <circle cx="29" cy="116" r="2.3" fill="#8e3a2b"/><circle cx="138" cy="116" r="2.3" fill="#141414"/><circle cx="246" cy="116" r="2.3" fill="#141414"/>
  </svg>
  <div class="abs" style="left:36px;top:52px;width:90px"><div style="font-size:5px;font-weight:700;color:var(--maroon)">Your Text Here</div><div class="tiny">Short note about this point, kept brief and clear for the reader.</div></div>
  <div class="abs" style="left:145px;top:52px;width:90px"><div style="font-size:5px;font-weight:700;color:var(--black)">Your Text Here</div><div class="tiny">Short note about this point, kept brief and clear for the reader.</div></div>
  <div class="abs" style="left:253px;top:52px;width:85px"><div style="font-size:5px;font-weight:700;color:var(--black)">Your Text Here</div><div class="tiny">Short note about this point, kept brief and clear for the reader.</div></div>
  <div class="abs" style="left:36px;top:113px;width:90px"><div style="font-size:5px;font-weight:700;color:var(--maroon)">Your Text Here</div><div class="tiny">Short note about this point, kept brief and clear for the reader.</div></div>
  <div class="abs" style="left:145px;top:113px;width:90px"><div style="font-size:5px;font-weight:700;color:var(--black)">Your Text Here</div><div class="tiny">Short note about this point, kept brief and clear for the reader.</div></div>
  <div class="abs" style="left:253px;top:113px;width:85px"><div style="font-size:5px;font-weight:700;color:var(--black)">Your Text Here</div><div class="tiny">Short note about this point, kept brief and clear for the reader.</div></div>
  <div class="foot-logo">KAVORA<span>Properties</span></div>
  <div class="foot-copy">© Copyright 2024 Kavora. All rights reserved.</div>
</section>

<!-- 7 Portfolio grid -->
<section class="slide" style="left:4px;top:402px">
  <div class="s-title">PORTFOLIO</div>
  <svg class="corner" viewBox="0 0 30 30" aria-hidden="true"><polygon points="0,0 30,0 30,30" fill="#8e3a2b"/><text x="24" y="9" font-size="4" fill="#fff">7</text></svg>
  <div class="ph ph-sky" style="left:19px;top:36px;width:57px;height:65px" role="img" aria-label="Photograph of a completed housing block"></div>
  <div class="ph ph-grey" style="left:83px;top:36px;width:57px;height:65px" role="img" aria-label="Photograph of a steel and glass facade"></div>
  <div class="ph ph-sky" style="left:146px;top:36px;width:57px;height:65px" role="img" aria-label="Photograph of a roof structure under construction"></div>
  <div class="ph ph-site" style="left:19px;top:104px;width:57px;height:66px" role="img" aria-label="Photograph of new homes in a development"></div>
  <div class="ph ph-site" style="left:83px;top:104px;width:57px;height:66px" role="img" aria-label="Photograph of a row of small houses"></div>
  <div class="ph ph-site" style="left:146px;top:104px;width:57px;height:66px" role="img" aria-label="Photograph of a housing estate at sunset"></div>
  <div class="ph" style="left:206px;top:36px;width:123px;height:134px;background:linear-gradient(180deg,#a9bfd2 0%,#c96a45 45%,#9c4a2f 100%)" role="img" aria-label="Photograph of an orange brick house with white window"></div>
  <div class="foot-logo">KAVORA<span>Properties</span></div>
  <div class="foot-copy">© Copyright 2024 Kavora. All rights reserved.</div>
</section>

<!-- 8 Portfolio cards -->
<section class="slide" style="left:357px;top:402px">
  <div class="s-title">PORTFOLIO</div>
  <svg class="corner" viewBox="0 0 30 30" aria-hidden="true"><polygon points="0,0 30,0 30,30" fill="#8e3a2b"/><text x="24" y="9" font-size="4" fill="#fff">8</text></svg>
  <div class="abs" style="left:34px;top:40px;width:64px;height:2px;background:var(--maroon)"></div>
  <div class="ph ph-home" style="left:34px;top:42px;width:64px;height:93px" role="img" aria-label="Photograph of a beige apartment block"></div>
  <div class="abs" style="left:64px;top:138px;width:4px;height:4px;background:var(--maroon)"></div>
  <div class="abs ph-label" style="left:34px;top:148px;width:64px;color:var(--maroon);font-weight:400;font-size:4.5px">Portfolio Nam</div>
  <div class="abs" style="left:34px;top:163px;width:64px;height:5px;background:var(--maroon)"></div>

  <div class="abs" style="left:104px;top:40px;width:64px;height:2px;background:var(--black)"></div>
  <div class="ph" style="left:104px;top:42px;width:64px;height:93px;background:linear-gradient(180deg,#9db8d3 0%,#2a5fb0 50%,#c8c2b8 100%)" role="img" aria-label="Photograph of a building with a blue stair tower"></div>
  <div class="abs" style="left:134px;top:138px;width:4px;height:4px;background:var(--black)"></div>
  <div class="abs ph-label" style="left:104px;top:148px;width:64px;font-weight:400;font-size:4.5px">Portfolio Name</div>
  <div class="abs" style="left:104px;top:163px;width:64px;height:5px;background:var(--black)"></div>

  <div class="abs" style="left:175px;top:40px;width:64px;height:2px;background:var(--slate)"></div>
  <div class="ph" style="left:175px;top:42px;width:64px;height:93px;background:linear-gradient(180deg,#9db3c4 0%,#b5523a 50%,#555 100%)" role="img" aria-label="Photograph of a red and grey apartment block"></div>
  <div class="abs" style="left:205px;top:138px;width:4px;height:4px;background:var(--slate)"></div>
  <div class="abs ph-label" style="left:175px;top:148px;width:64px;font-weight:400;font-size:4.5px">Portfolio Name</div>
  <div class="abs" style="left:175px;top:163px;width:64px;height:5px;background:var(--slate)"></div>

  <div class="abs" style="left:246px;top:40px;width:64px;height:2px;background:var(--maroon)"></div>
  <div class="ph" style="left:246px;top:42px;width:64px;height:93px;background:linear-gradient(180deg,#6b2b22 0%,#c9b9a4 60%,#e5d9c8 100%)" role="img" aria-label="Photograph of an office interior with tiled floor"></div>
  <div class="abs" style="left:276px;top:138px;width:4px;height:4px;background:var(--maroon)"></div>
  <div class="abs ph-label" style="left:246px;top:148px;width:64px;color:var(--maroon);font-weight:400;font-size:4.5px">Portfolio Name</div>
  <div class="abs" style="left:246px;top:163px;width:64px;height:5px;background:var(--maroon)"></div>
  <div class="foot-logo">KAVORA<span>Properties</span></div>
  <div class="foot-copy">© Copyright 2024 Kavora. All rights reserved.</div>
</section>

<!-- 9 Portfolio mixed -->
<section class="slide" style="left:710px;top:402px">
  <div class="s-title">PORTFOLIO</div>
  <svg class="corner" viewBox="0 0 30 30" aria-hidden="true"><polygon points="0,0 30,0 30,30" fill="#8e3a2b"/><text x="24" y="9" font-size="4" fill="#fff">9</text></svg>
  <div class="ph ph-int" style="left:16px;top:38px;width:57px;height:65px" role="img" aria-label="Photograph of an office interior"></div>
  <div class="cell-text" style="left:78px;top:38px;width:91px;height:65px;background:var(--maroon)"><h4>Portfolio Name</h4><p>Our short and precise slogan describes our approach to the tasks and solutions, and it is a summary of those</p></div>
  <div class="cell-text" style="left:175px;top:38px;width:91px;height:65px;background:var(--black)"><h4>Portfolio Name</h4><p>Our short and precise slogan describes our approach to the tasks and solutions, and it is a summary of those</p></div>
  <div class="ph ph-grey" style="left:272px;top:38px;width:57px;height:65px" role="img" aria-label="Photograph of an empty office hall"></div>
  <div class="ph ph-int" style="left:16px;top:107px;width:57px;height:65px" role="img" aria-label="Photograph of a reception counter"></div>
  <div class="cell-text" style="left:78px;top:107px;width:91px;height:65px;background:var(--slate)"><h4>Portfolio Name</h4><p>Our short and precise slogan describes our approach to the tasks and solutions, and it is a summary of those</p></div>
  <div class="cell-text" style="left:175px;top:107px;width:91px;height:65px;background:var(--maroon)"><h4>Portfolio Name</h4><p>Our short and precise slogan describes our approach to the tasks and solutions, and it is a summary of those</p></div>
  <div class="ph" style="left:272px;top:107px;width:57px;height:65px;background:linear-gradient(180deg,#9db8d3 0%,#2a5fb0 55%,#c8c2b8 100%)" role="img" aria-label="Photograph of a building with a blue stair tower"></div>
  <div class="foot-logo">KAVORA<span>Properties</span></div>
  <div class="foot-copy">© Copyright 2024 Kavora. All rights reserved.</div>
</section>

<!-- 10 Gallery -->
<section class="slide" style="left:4px;top:601px">
  <div class="s-title">GALLERY&nbsp; SERVICES SAMPLE</div>
  <svg class="corner" viewBox="0 0 30 30" aria-hidden="true"><polygon points="0,0 30,0 30,30" fill="#8e3a2b"/><text x="22" y="9" font-size="4" fill="#fff">10</text></svg>
  <div class="ph ph-int" style="left:15px;top:44px;width:102px;height:89px" role="img" aria-label="Photograph of an office with red walls"></div>
  <div class="abs ph-label" style="left:15px;top:140px;width:102px;color:var(--maroon);font-weight:400;font-size:4.5px">SERVICES Name</div>
  <div class="abs" style="left:15px;top:150px;width:102px;height:4px;background:var(--maroon)"></div>
  <div class="ph ph-road" style="left:126px;top:44px;width:102px;height:89px" role="img" aria-label="Photograph of a paving machine on a road site"></div>
  <div class="abs ph-label" style="left:126px;top:140px;width:102px;font-weight:400;font-size:4.5px">SERVICES Name</div>
  <div class="abs" style="left:126px;top:150px;width:102px;height:4px;background:var(--black)"></div>
  <div class="ph ph-home" style="left:237px;top:44px;width:102px;height:89px" role="img" aria-label="Photograph of a living room with grey sofa"></div>
  <div class="abs ph-label" style="left:237px;top:140px;width:102px;font-weight:400;font-size:4.5px">SERVICES Name</div>
  <div class="abs" style="left:237px;top:150px;width:102px;height:4px;background:var(--slate)"></div>
  <div class="foot-logo">KAVORA<span>Properties</span></div>
  <div class="foot-copy">© Copyright 2024 Kavora. All rights reserved.</div>
</section>

<!-- 11 Important points -->
<section class="slide" style="left:357px;top:601px">
  <div class="s-title">IMPORTANT POINTS</div>
  <svg class="corner" viewBox="0 0 30 30" aria-hidden="true"><polygon points="0,0 30,0 30,30" fill="#8e3a2b"/><text x="22" y="9" font-size="4" fill="#fff">11</text></svg>
  <div class="ph ph-home" style="left:18px;top:48px;width:75px;height:87px" role="img" aria-label="Photograph of a lounge with a green chair"></div>
  <div class="ph ph-site" style="left:96px;top:48px;width:75px;height:87px" role="img" aria-label="Photograph of a row of townhouses"></div>
  <div class="ph" style="left:174px;top:48px;width:75px;height:87px;background:linear-gradient(180deg,#9fb4c9 0%,#8a8a8a 50%,#3aa6d8 100%)" role="img" aria-label="Photograph of a modern house with a pool"></div>
  <div class="ph ph-grey" style="left:253px;top:48px;width:75px;height:87px" role="img" aria-label="Photograph of a covered patio structure"></div>
  <div class="abs" style="left:18px;top:140px;width:75px;text-align:center"><div style="font-size:4.5px;color:var(--maroon)">1 Points</div><div class="tiny" style="margin-top:4px">Many short notes can sit here to explain this point in brief</div></div>
  <div class="abs" style="left:96px;top:140px;width:75px;text-align:center"><div style="font-size:4.5px">2 Points</div><div class="tiny" style="margin-top:4px">Many short notes can sit here to explain this point in brief</div></div>
  <div class="abs" style="left:174px;top:140px;width:75px;text-align:center"><div style="font-size:4.5px">3 Points</div><div class="tiny" style="margin-top:4px">Many short notes can sit here to explain this point in brief</div></div>
  <div class="abs" style="left:253px;top:140px;width:75px;text-align:center"><div style="font-size:4.5px;color:var(--maroon)">4 Points</div><div class="tiny" style="margin-top:4px">Many short notes can sit here to explain this point in brief</div></div>
  <div class="foot-logo">KAVORA<span>Properties</span></div>
  <div class="foot-copy">© Copyright 2024 Kavora. All rights reserved.</div>
</section>

<!-- 12 Mission & vision -->
<section class="slide" style="left:710px;top:601px">
  <div class="s-title">OUR MISSION &amp; VISION</div>
  <svg class="corner" viewBox="0 0 30 30" aria-hidden="true"><polygon points="0,0 30,0 30,30" fill="#8e3a2b"/><text x="22" y="9" font-size="4" fill="#fff">12</text></svg>
  <div class="ph ph-site" style="left:0;top:52px;width:86px;height:114px" role="img" aria-label="Photograph of a dirt road beside trees"></div>
  <div class="abs" style="left:86px;top:39px;width:87px;height:127px;background:var(--maroon)"></div>
  <div class="abs" style="left:173px;top:39px;width:86px;height:127px;background:var(--slate)"></div>
  <div class="ph ph-sky" style="left:259px;top:39px;width:86px;height:127px" role="img" aria-label="Photograph of a multi-storey building under construction"></div>
  <svg class="abs" style="left:0;top:0" width="345" height="194" aria-hidden="true">
    <circle cx="86" cy="68" r="13" fill="#8e3a2b" stroke="#fff" stroke-width="1.2"/>
    <path d="M79 69 L86 62 L93 69 M81 68 V75 H91 V68" fill="#fff"/>
    <circle cx="259" cy="68" r="13" fill="#3a3d43" stroke="#fff" stroke-width="1.2"/>
    <path d="M252 69 L259 62 L266 69 M254 68 V75 H264 V68" fill="none" stroke="#fff" stroke-width="1.2"/>
    <circle cx="259" cy="70" r="2" fill="#fff"/>
  </svg>
  <div class="abs white" style="left:100px;top:99px;width:72px"><div style="font-size:8px">Mission</div><div style="font-size:3.8px;line-height:1.8;margin-top:2px">This is a sample text. You simply add your own text and description here.</div></div>
  <div class="abs white" style="left:183px;top:99px;width:72px"><div style="font-size:8px">Vision</div><div style="font-size:3.8px;line-height:1.8;margin-top:2px">This is a sample text. You simply add your own text and description here.</div></div>
  <div class="foot-logo">KAVORA<span>Properties</span></div>
  <div class="foot-copy">© Copyright 2024 Kavora. All rights reserved.</div>
</section>

<!-- 13 Portfolio tiles -->
<section class="slide" style="left:4px;top:800px">
  <div class="s-title">PORTFOLIO</div>
  <svg class="corner" viewBox="0 0 30 30" aria-hidden="true"><polygon points="0,0 30,0 30,30" fill="#8e3a2b"/><text x="22" y="9" font-size="4" fill="#fff">13</text></svg>
  <div class="ph ph-home" style="left:20px;top:47px;width:57px;height:57px" role="img" aria-label="Photograph of a beige apartment block"></div>
  <div class="abs white" style="left:84px;top:47px;width:57px;height:57px;background:var(--black)"><span class="num">02</span><span class="ph-label">TITLE PLACEHOLDER</span></div>
  <div class="ph ph-grey" style="left:147px;top:47px;width:57px;height:57px" role="img" aria-label="Photograph of modern grey townhouses"></div>
  <div class="abs white" style="left:210px;top:47px;width:57px;height:57px;background:var(--maroon)"><span class="num">04</span><span class="ph-label">TITLE PLACEHOLDER</span></div>
  <div class="ph ph-sky" style="left:274px;top:47px;width:57px;height:57px" role="img" aria-label="Photograph of houses under construction"></div>
  <div class="abs white" style="left:20px;top:110px;width:57px;height:57px;background:var(--maroon)"><span class="num">01</span><span class="ph-label">TITLE PLACEHOLDER</span></div>
  <div class="ph ph-road" style="left:84px;top:110px;width:57px;height:57px" role="img" aria-label="Photograph of a paving machine"></div>
  <div class="abs white" style="left:147px;top:110px;width:57px;height:57px;background:var(--slate)"><span class="num">03</span><span class="ph-label">TITLE PLACEHOLDER</span></div>
  <div class="ph ph-sky" style="left:210px;top:110px;width:57px;height:57px" role="img" aria-label="Photograph of a steel framework on site"></div>
  <div class="abs white" style="left:274px;top:110px;width:57px;height:57px;background:var(--black)"><span class="num">05</span><span class="ph-label">TITLE PLACEHOLDER</span></div>
  <div class="foot-logo">KAVORA<span>Properties</span></div>
  <div class="foot-copy">© Copyright 2024 Kavora. All rights reserved.</div>
</section>

<!-- 14 Mosaic -->
<section class="slide" style="left:357px;top:800px">
  <div class="cell-text" style="left:0;top:0;width:172px;height:59px;background:var(--maroon);padding:7px 20px"><p style="text-align:justify">We plan and deliver projects with care, skill and steady communication. Every site follows strict safety rules, and each handover meets the standard our clients expect.</p></div>
  <div class="ph ph-road" style="left:172px;top:0;width:173px;height:59px" role="img" aria-label="Aerial photograph of a highway interchange"></div>
  <div class="ph ph-site" style="left:0;top:59px;width:172px;height:77px" role="img" aria-label="Aerial photograph of a housing estate"></div>
  <div class="cell-text" style="left:172px;top:59px;width:173px;height:77px;background:var(--black);padding:14px 20px"><p style="text-align:justify">We plan and deliver projects with care, skill and steady communication. Every site follows strict safety rules, and each handover meets the standard our clients expect.</p></div>
  <div class="cell-text" style="left:0;top:136px;width:172px;height:58px;background:var(--slate);padding:7px 20px"><p style="text-align:justify">We plan and deliver projects with care, skill and steady communication. Every site follows strict safety rules, and each handover meets the standard our clients expect.</p></div>
  <div class="ph ph-int" style="left:172px;top:136px;width:173px;height:58px" role="img" aria-label="Photograph of red brick apartment blocks"></div>
</section>

<!-- 15 Four columns -->
<section class="slide" style="left:710px;top:800px">
  <div class="s-title">YOUR TITLE HERE</div>
  <svg class="corner" viewBox="0 0 30 30" aria-hidden="true"><polygon points="0,0 30,0 30,30" fill="#8e3a2b"/><text x="22" y="9" font-size="4" fill="#fff">15</text></svg>
  <div class="cell-text" style="left:0;top:53px;width:87px;height:103px;background:var(--maroon);text-align:center;padding-top:28px"><h4 style="font-weight:400">Heading Here</h4><p style="text-align:justify;font-size:3.7px">Add a short summary of this topic here. Keep it clear and useful, so each reader knows the key idea and what it means for them.</p></div>
  <div class="cell-text" style="left:87px;top:53px;width:86px;height:103px;background:var(--black);text-align:center;padding-top:28px"><h4 style="font-weight:400">Heading Here</h4><p style="text-align:justify;font-size:3.7px">Add a short summary of this topic here. Keep it clear and useful, so each reader knows the key idea and what it means for them.</p></div>
  <div class="cell-text" style="left:173px;top:53px;width:86px;height:103px;background:var(--slate);text-align:center;padding-top:28px"><h4 style="font-weight:400">Heading Here</h4><p style="text-align:justify;font-size:3.7px">Add a short summary of this topic here. Keep it clear and useful, so each reader knows the key idea and what it means for them.</p></div>
  <div class="cell-text" style="left:259px;top:53px;width:86px;height:103px;background:var(--maroon);text-align:center;padding-top:28px"><h4 style="font-weight:400">Heading Here</h4><p style="text-align:justify;font-size:3.7px">Add a short summary of this topic here. Keep it clear and useful, so each reader knows the key idea and what it means for them.</p></div>
  <svg class="abs" style="left:0;top:0" width="345" height="194" aria-hidden="true" fill="none" stroke="#fff" stroke-width="1">
    <circle cx="43" cy="70" r="6"/><path d="M37 70 H49 M43 64 V76"/>
    <circle cx="130" cy="68" r="4"/><path d="M130 72 V77"/>
    <circle cx="216" cy="68" r="3"/><path d="M210 77 Q216 70 222 77"/>
    <rect x="296" y="65" width="12" height="10"/><path d="M298 69 H306 M298 72 H304"/>
  </svg>
  <div class="foot-logo">KAVORA<span>Properties</span></div>
  <div class="foot-copy">© Copyright 2024 Kavora. All rights reserved.</div>
</section>

<!-- 16 Differences -->
<section class="slide" style="left:4px;top:1000px">
  <div class="s-title">OUR DIFFERENCES</div>
  <svg class="corner" viewBox="0 0 30 30" aria-hidden="true"><polygon points="0,0 30,0 30,30" fill="#8e3a2b"/><text x="22" y="9" font-size="4" fill="#fff">16</text></svg>
  <div class="abs" style="left:22px;top:51px;width:309px;height:101px;background:var(--maroon)"></div>
  <div class="ph ph-int" style="left:204px;top:65px;width:117px;height:75px" role="img" aria-label="Photograph of an office with desks and red walls"></div>
  <svg class="abs" style="left:0;top:0" width="345" height="194" aria-hidden="true" fill="none" stroke="#fff" stroke-width="1">
    <path d="M38 72 L44 66 M40 68 L43 71"/>
    <circle cx="41" cy="92" r="3"/><circle cx="41" cy="92" r="1" fill="#fff"/>
    <path d="M38 115 L44 109"/>
    <circle cx="40" cy="131" r="2.5"/><path d="M42 133 L45 136"/>
  </svg>
  <div class="abs white" style="left:54px;top:66px;width:140px;font-size:4.2px;line-height:1.35">We finish on schedule and within the agreed budget, every time.</div>
  <div class="abs white" style="left:54px;top:87px;width:140px;font-size:4.2px;line-height:1.35">Our site teams follow strict safety rules to protect every worker.</div>
  <div class="abs white" style="left:54px;top:108px;width:140px;font-size:4.2px;line-height:1.35">We use trusted materials that stand up to years of daily use.</div>
  <div class="abs white" style="left:54px;top:127px;width:140px;font-size:4.2px;line-height:1.35">Clients get clear updates at each stage of the project.</div>
  <div class="foot-logo">KAVORA<span>Properties</span></div>
  <div class="foot-copy">© Copyright 2024 Kavora. All rights reserved.</div>
</section>

<!-- 17 Text & bullets -->
<section class="slide" style="left:357px;top:1000px">
  <div class="s-title">TEXT &amp; BULLET AREA</div>
  <svg class="corner" viewBox="0 0 30 30" aria-hidden="true"><polygon points="0,0 30,0 30,30" fill="#8e3a2b"/><text x="22" y="9" font-size="4" fill="#fff">17</text></svg>
  <div class="abs" style="left:20px;top:51px;width:95px"><div style="font-size:6px;color:var(--maroon);margin-bottom:7px">Heading Goes Here</div>
    <div class="tiny" style="margin-bottom:5px">Use this space for a short opening about the topic and why it matters to the project team.</div>
    <div class="tiny" style="margin-bottom:5px">Add a second note that supports the point above with one clear detail.</div>
    <div class="tiny">Close with a final line that sums up the idea for the reader.</div></div>
  <svg class="abs" style="left:0;top:0" width="345" height="194" aria-hidden="true">
    <circle cx="134" cy="57" r="6" fill="#8e3a2b"/><circle cx="134" cy="86" r="6" fill="#141414"/><circle cx="134" cy="114" r="6" fill="#3a3d43"/><circle cx="134" cy="142" r="6" fill="#8e3a2b"/>
    <circle cx="243" cy="57" r="6" fill="#8e3a2b"/><circle cx="243" cy="86" r="6" fill="#3a3d43"/><circle cx="243" cy="114" r="6" fill="#141414"/><circle cx="243" cy="142" r="6" fill="#8e3a2b"/>
    <g stroke="#fff" stroke-width="1" fill="none">
      <path d="M131 57 H137 M134 54 V60"/><path d="M131 89 V86 M134 89 V83 M137 89 V85"/><circle cx="134" cy="113" r="2"/><circle cx="134" cy="142" r="2.5"/>
      <circle cx="242" cy="56" r="2"/><path d="M243.5 57.5 L246 60"/><path d="M240 89 L246 83"/><path d="M240 117 L246 111"/><circle cx="243" cy="142" r="2"/>
    </g>
  </svg>
  <div class="abs" style="left:144px;top:52px;width:85px"><div style="font-size:6px;color:var(--maroon)">Your Text Here</div><div class="tiny" style="font-size:3px">Brief supporting line for this item goes right here.</div></div>
  <div class="abs" style="left:144px;top:81px;width:85px"><div style="font-size:6px">Your Text Here</div><div class="tiny" style="font-size:3px">Brief supporting line for this item goes right here.</div></div>
  <div class="abs" style="left:144px;top:109px;width:85px"><div style="font-size:6px">Your Text Here</div><div class="tiny" style="font-size:3px">Brief supporting line for this item goes right here.</div></div>
  <div class="abs" style="left:144px;top:137px;width:85px"><div style="font-size:6px;color:var(--maroon)">Your Text Here</div><div class="tiny" style="font-size:3px">Brief supporting line for this item goes right here.</div></div>
  <div class="abs" style="left:253px;top:52px;width:85px"><div style="font-size:6px;color:var(--maroon)">Your Text Here</div><div class="tiny" style="font-size:3px">Brief supporting line for this item goes right here.</div></div>
  <div class="abs" style="left:253px;top:81px;width:85px"><div style="font-size:6px">Your Text Here</div><div class="tiny" style="font-size:3px">Brief supporting line for this item goes right here.</div></div>
  <div class="abs" style="left:253px;top:109px;width:85px"><div style="font-size:6px">Your Text Here</div><div class="tiny" style="font-size:3px">Brief supporting line for this item goes right here.</div></div>
  <div class="abs" style="left:253px;top:137px;width:85px"><div style="font-size:6px;color:var(--maroon)">Your Text Here</div><div class="tiny" style="font-size:3px">Brief supporting line for this item goes right here.</div></div>
  <div class="foot-logo">KAVORA<span>Properties</span></div>
  <div class="foot-copy">© Copyright 2024 Kavora. All rights reserved.</div>
</section>

<!-- 18 Clients -->
<section class="slide" style="left:710px;top:1000px">
  <div class="client" style="left:15px;top:27px">Halden</div>
  <div class="client" style="left:104px;top:27px">Norvik</div>
  <div class="client" style="left:193px;top:27px">Brightfold</div>
  <div class="client" style="left:280px;top:27px;width:60px">Ashgrove</div>
  <div class="client" style="left:15px;top:92px">Lumera</div>
  <div class="client" style="left:270px;top:92px">Corvale</div>
  <div class="client" style="left:15px;top:157px">Verity</div>
  <div class="client" style="left:104px;top:157px">Tessin</div>
  <div class="client" style="left:193px;top:157px">Marlow Co</div>
  <div class="client" style="left:273px;top:157px">Oakmere</div>
  <div class="abs white" style="left:87px;top:66px;width:172px;height:63px;background:var(--maroon);text-align:center;font-size:16px;line-height:1.2;padding-top:8px">OUR AWESOME<br>CLIENT</div>
</section>

</div>
</body>
</html>
```